" A proprietária é a Lorena Bastolli, Biomedica, pós graduada em estética e Mestra pela Universidade de Vale Dourado. Temos trabalhando conosco uma fisioterapeuta, uma esteticista, uma estagiária em biomedica, uma secretária, e temos parceria com uma Nutricionista com PHD e uma Médica especialista em Endocrinologia, ambas atendem na clínica uma vez por semana. "

```html
<!DOCTYPE html>
<html lang="pt-BR">
<head>
<meta charset="utf-8">
<title>Lorena Bastolli – Cartão de visita</title>
<link rel="stylesheet" href="https://fonts.googleapis.com/css2?family=Open+Sans:wght@400;600;700&display=swap">
<style>
  :root {
    --bg: #e6e6e4;
    --card-light: #ffffff;
    --card-dark: #4b4b4d;
    --pattern-light: #eeeeee;
    --pattern-dark: #555557;
    --ink: #4a4a4a;
    --ink-soft: #6b6b6b;
    --gold: #c9973a;
    --white: #ffffff;
    --muted-on-dark: #b9b9b9;
  }
  * { box-sizing: border-box; margin: 0; padding: 0; }
  html, body { width: 1200px; height: 1200px; overflow: hidden; }
  body {
    background: var(--bg);
    font-family: "Open Sans", Arial, sans-serif;
    position: relative;
  }
  .card {
    position: absolute;
    left: 190px;
    width: 820px;
    height: 456px;
    border-radius: 4px;
    overflow: hidden;
    box-shadow: 0 10px 30px rgba(0,0,0,0.12);
  }
  .card--front { top: 110px; background: var(--card-light); }
  .card--back { top: 634px; background: var(--card-dark); }

  .front-pattern {
    position: absolute;
    top: 0; left: 150px; right: 0;
    height: 150px;
    background: linear-gradient(180deg, var(--pattern-light), rgba(238,238,238,0));
  }
  .identity {
    position: absolute;
    left: 56px; top: 190px;
    display: flex; align-items: center; gap: 22px;
  }
  .brand-dot {
    width: 62px; height: 62px;
    border-radius: 50%;
    border: 3px solid var(--gold);
  }
  .identity-name { font-size: 30px; font-weight: 700; color: var(--ink); line-height: 1.1; }
  .identity-role { font-size: 26px; font-weight: 400; color: var(--gold); line-height: 1.2; }

  .contact-list {
    position: absolute; left: 56px; top: 300px;
    list-style: none; font-size: 17px; color: var(--ink-soft);
  }
  .contact-list li { display: flex; align-items: flex-start; gap: 10px; margin-bottom: 10px; line-height: 1.35; }
  .contact-list svg { flex: none; margin-top: 2px; }

  .online {
    position: absolute; right: 46px; top: 190px;
    text-align: left; font-size: 17px; color: var(--ink-soft); line-height: 1.9;
  }
  .online-handle { display: flex; align-items: center; gap: 10px; }
  .online-handle span.marker {
    width: 12px; height: 12px; border-radius: 50%; background: var(--gold); display: inline-block;
  }

  .back-pattern {
    position: absolute; top: 0; bottom: 0; left: 50px;
    width: 170px;
    background: linear-gradient(90deg, var(--pattern-dark), rgba(85,85,87,0.4));
  }
  .back-identity {
    position: absolute; right: 70px; top: 150px;
    display: flex; align-items: center; gap: 24px;
  }
  .back-identity .brand-dot { width: 70px; height: 70px; }
  .back-name {
    font-size: 40px; font-weight: 600; color: var(--white); line-height: 1.05;
  }
  .back-tagline {
    margin-top: 8px; font-size: 13px; letter-spacing: 3px;
    color: var(--muted-on-dark); text-transform: uppercase;
  }
</style>
</head>
<body>

  <section class="card card--front" aria-label="Frente do cartão">
    <div class="front-pattern" role="img" aria-label="Padrão floral decorativo em cinza claro"></div>

    <div class="identity">
      <span class="brand-dot"></span>
      <div>
        <p class="identity-name">Lorena Bastolli</p>
        <p class="identity-role">biomédica</p>
      </div>
    </div>

    <ul class="contact-list">
      <li>
        <svg width="16" height="16" viewBox="0 0 16 16" aria-hidden="true"><path d="M3 1.5l3 .5 1 3-2 1.3a8 8 0 0 0 4.7 4.7L11 9l3 1 .5 3-1.5 1.5C7.5 14.5 1.5 8.5 1.5 3z" fill="var(--gold)"/></svg>
        +55 (16) 99287-3150
      </li>
      <li>
        <svg width="16" height="18" viewBox="0 0 16 18" aria-hidden="true"><path d="M8 1a5.5 5.5 0 0 0-5.5 5.5C2.5 11 8 17 8 17s5.5-6 5.5-10.5A5.5 5.5 0 0 0 8 1zm0 7.5a2 2 0 1 1 0-4 2 2 0 0 1 0 4z" fill="var(--gold)"/></svg>
        <span>Rua das Acácias, 1111<br>Vale Dourado - SP</span>
      </li>
    </ul>

    <div class="online">
      <p class="online-handle"><span class="marker"></span>clinicalorenabastolli</p>
      <p>www.lorenabastolli.com.br</p>
    </div>
  </section>

  <section class="card card--back" aria-label="Verso do cartão">
    <div class="back-pattern" role="img" aria-label="Coluna de padrão floral decorativo em cinza"></div>
    <div class="back-identity">
      <span class="brand-dot"></span>
      <div>
        <p class="back-name">Lorena<br>Bastolli</p>
        <p class="back-tagline">biomedicina estética</p>
      </div>
    </div>
  </section>

</body>
</html>
```